Health & Nutrition - Business Cards

Needs to look new-age, simple, and elegant. The cards are for my services/counsel in health and nutrition - which include mind, body, and soul. I would like to see something clean and simple but beautiful. Can have a plain background or with a pattern but I don't want it to take away from my contact details. Therefore, my info can be on the back of the card and a nice front design. I really like the flower of life symbol. The name of my business is called Willow Lantern.

Target Market(s)

Clients - men & women age 20-60. Adults, parents, teachers, sick individuals seeking nutrient counseling and dietary management.

Industry/Entity Type

Nutritionist

Contact Information for Business Card

Tomas Brindle
Cell: 345-582-7046
Email: tbrindle@mailvane.net

Colors
33a6d7
33b8a4
add136
ffffff
5c5c5c
f04a50
fbee3f
cedeed
85cae6

Requirements
Nice to have
• Maybe it can have some sort of sacred geometry as well, but not required. Nice to have the colors that I choose in the project but feel free to come up with your own use of colors. Thanks! =)

```html
<!DOCTYPE html>
<html lang="en">
<head>
<meta charset="utf-8">
<title>Willow Lantern – Business Cards</title>
<link href="https://fonts.googleapis.com/css2?family=Lato:wght@400;700&display=swap" rel="stylesheet">
<style>
  :root {
    --backdrop: #3a3331;
    --card: #0b0b0b;
    --card-edge: #1a1a1a;
    --teal: #33b8a4;
    --lime: #add136;
    --text-light: #d9d9d9;
    --silver: #d6d6d6;
    --divider: #1f1f1f;
  }
  * { box-sizing: border-box; margin: 0; padding: 0; }
  html, body {
    width: 1200px;
    height: 844px;
    overflow: hidden;
    background: var(--backdrop);
    font-family: "Lato", sans-serif;
  }
  .stage {
    position: relative;
    width: 1200px;
    height: 844px;
  }
  .card {
    position: absolute;
    top: 272px;
    width: 520px;
    height: 300px;
    background: var(--card);
    border: 1px solid var(--card-edge);
    box-shadow: 0 10px 30px rgba(0, 0, 0, 0.45);
  }
  /* Contact side */
  .card--contact { left: 50px; }
  .card--contact .brand-block {
    position: absolute;
    left: 0; top: 0;
    width: 270px; height: 100%;
    display: flex;
    align-items: center;
    justify-content: center;
    gap: 12px;
  }
  .brand-dot {
    width: 18px; height: 18px;
    border-radius: 50%;
    background: var(--teal);
    flex: none;
  }
  .brand-name {
    color: var(--lime);
    font-weight: 700;
    font-size: 24px;
    letter-spacing: 0.5px;
  }
  .divider {
    position: absolute;
    left: 270px; top: 0;
    width: 1px; height: 100%;
    background: var(--divider);
  }
  .contact-block {
    position: absolute;
    left: 296px; top: 100px;
  }
  .person-name {
    color: var(--teal);
    font-size: 19px;
    font-weight: 400;
    letter-spacing: 0.6px;
    text-transform: uppercase;
    margin-bottom: 26px;
  }
  .contact-line {
    display: flex;
    align-items: center;
    gap: 7px;
    color: var(--text-light);
    font-size: 14px;
    line-height: 20px;
    margin-bottom: 4px;
  }
  .contact-line svg { width: 12px; height: 12px; flex: none; }
  /* Brand side */
  .card--brand { left: 630px; }
  .card--brand .brand-block {
    position: absolute;
    inset: 0;
    display: flex;
    flex-direction: column;
    align-items: center;
    justify-content: center;
    gap: 22px;
  }
  .brand-ring {
    width: 64px; height: 64px;
    border-radius: 50%;
    border: 9px solid var(--silver);
  }
  .card--brand .brand-name {
    color: var(--silver);
    font-weight: 400;
    font-size: 22px;
    letter-spacing: 4px;
    text-transform: uppercase;
  }
</style>
</head>
<body>
<main class="stage">
  <section class="card card--contact">
    <div class="brand-block">
      <span class="brand-dot"></span>
      <span class="brand-name">Willow Lantern</span>
    </div>
    <div class="divider"></div>
    <div class="contact-block">
      <h1 class="person-name">Tomas Brindle</h1>
      <p class="contact-line">
        <svg viewBox="0 0 12 12" aria-hidden="true"><path fill="#33b8a4" d="M2.5 1 4.5 1 5.2 3.6 4 4.6C4.6 6 6 7.4 7.4 8L8.4 6.8 11 7.5 11 9.5C11 10.3 10.3 11 9.5 11 5 11 1 7 1 2.5 1 1.7 1.7 1 2.5 1Z"/></svg>
        345-582-7046
      </p>
      <p class="contact-line">
        <svg viewBox="0 0 12 12" aria-hidden="true"><rect x="0.5" y="2" width="11" height="8" fill="#33b8a4"/><path d="M0.8 2.4 6 6.6 11.2 2.4" fill="none" stroke="#0b0b0b" stroke-width="1"/></svg>
        tbrindle@mailvane.net
      </p>
    </div>
  </section>

  <section class="card card--brand">
    <div class="brand-block">
      <span class="brand-ring"></span>
      <span class="brand-name">Willow Lantern</span>
    </div>
  </section>
</main>
</body>
</html>
```